Startup Drone Platform Company business card

We are needing a business card design for our employees. We are a startup drone platform. We are looking for a business card that has our logo on one side, with the employee/company details on the opposite side. We are looking for something that is very eye catching, modern, and bold.

Target Market(s)

This will target both drone pilots and drone businesses, along with all the industries that could utilize drone services (aerial video, aerial photos, inspections, 3d mapping, etc).

Industry/Entity Type

Business

```html
<!DOCTYPE html>
<html lang="en">
<head>
<meta charset="utf-8">
<title>Rotorlane Business Card</title>
<link href="https://fonts.googleapis.com/css2?family=Open+Sans:wght@400;700&display=swap" rel="stylesheet">
<style>
  :root {
    --teal: #3fbbc9;
    --ink: #111111;
    --paper: #ffffff;
    --backdrop: #e9eaec;
  }
  html, body {
    margin: 0;
    padding: 0;
    width: 1200px;
    height: 902px;
    overflow: hidden;
    background: var(--backdrop);
    font-family: "Open Sans", Arial, sans-serif;
  }
  .card {
    position: absolute;
    left: 80px;
    top: 154px;
    width: 1040px;
    height: 594px;
    border-radius: 26px;
    overflow: hidden;
    background: var(--paper);
    box-shadow: 0 10px 30px rgba(0,0,0,0.15);
  }
  .card-shape {
    position: absolute;
    inset: 0;
  }
  .contact {
    position: absolute;
    left: 50px;
    top: 100px;
    color: var(--ink);
  }
  .contact-name {
    margin: 0;
    font-size: 36px;
    font-weight: 700;
    line-height: 1.1;
  }
  .contact-role {
    margin: 0;
    font-size: 26px;
    color: var(--paper);
    line-height: 1.1;
  }
  .contact-address {
    margin: 82px 0 0;
    font-size: 27px;
    line-height: 35px;
    font-style: normal;
  }
  .contact-lines {
    list-style: none;
    margin: 18px 0 0;
    padding: 0;
    font-size: 27px;
    line-height: 34px;
  }
  .contact-lines li {
    display: flex;
    align-items: center;
    gap: 10px;
  }
  .contact-icon {
    width: 29px;
    height: 29px;
    flex: none;
  }
  .contact-web {
    margin: 26px 0 0;
    font-size: 26px;
  }
  .brand {
    position: absolute;
    left: 560px;
    right: 0;
    top: 270px;
    display: flex;
    justify-content: center;
    align-items: center;
    gap: 18px;
  }
  .brand-dot {
    width: 30px;
    height: 30px;
    border-radius: 50%;
    background: var(--teal);
  }
  .brand-name {
    font-size: 40px;
    font-weight: 400;
    letter-spacing: 12px;
    color: var(--ink);
  }
</style>
</head>
<body>
  <section class="card">
    <svg class="card-shape" width="1040" height="594" viewBox="0 0 1040 594" aria-hidden="true">
      <path d="M0 0 H542 Q410 297 542 594 H0 Z" fill="var(--teal)"/>
      <path d="M547 0 Q415 297 547 594 Q433 297 547 0 Z" fill="var(--ink)"/>
    </svg>

    <div class="contact">
      <h1 class="contact-name">Employee Name</h1>
      <p class="contact-role">Director</p>
      <address class="contact-address">Your Adress Inc 2nd Lane<br>Ave Edison, NJ 00000</address>
      <ul class="contact-lines">
        <li>
          <svg class="contact-icon" viewBox="0 0 30 30" aria-hidden="true">
            <rect width="30" height="30" rx="5" fill="var(--paper)"/>
            <path d="M10 6 L13 6 L14 11 L12 13 Q14 17 17 19 L19 17 L24 18 L24 21 Q22 25 18 24 Q9 20 7 11 Q7 7 10 6 Z" fill="var(--teal)"/>
          </svg>
          <span>0123 456 789</span>
        </li>
        <li>
          <svg class="contact-icon" viewBox="0 0 30 30" aria-hidden="true">
            <rect width="30" height="30" rx="5" fill="var(--paper)"/>
            <rect x="6" y="9" width="18" height="13" fill="var(--teal)"/>
            <path d="M6 9 L15 17 L24 9" fill="none" stroke="var(--paper)" stroke-width="1.6"/>
          </svg>
          <span>info@yourmail.com</span>
        </li>
      </ul>
      <p class="contact-web">www.companyweb.com</p>
    </div>

    <div class="brand">
      <span class="brand-dot"></span>
      <span class="brand-name">ROTORLANE</span>
    </div>
  </section>
</body>
</html>
```